Trade Show Banner "Brindlequay"

1.7' x 3' vertical banner to complement trade show booth panels (3-panel tabletop booth attached). The word file (attached) is for text and not meant to imply design. We manage homeowner and condo associations that are run by volunteer boards of directors who already have full-time jobs or who may have no training in how to run an organization. It can be highly stressful and not very rewarding. We want this poster/banner to convey that feeling of stress along with a hope for relief and relaxation. Our logo is attached. The full logo is the top one in the file. You may also want to use the triangle (attached) in addition to or instead of the logo. Our corporate fonts are attached. Please let me know if you need additional information or if you feel like there is too much copy or any other thoughts or comments you have.

Target Market(s)

Volunteer boards of directors for homeowner and condo associations--all ages, genders, races, occupations.

Industry/Entity Type

Property Management

Other font styles liked:
• "Copper Lantern" is part of a trademark and should be in Mistral with the green from our logo

Requirements
Must have
• Simple, easy to read, don't clash with booth design
Nice to have
• convey the tension of stress contrasted with the feeling of relaxation and relief.

```html
<!DOCTYPE html>
<html lang="en">
<head>
<meta charset="utf-8">
<title>Brindlequay – For Board Members</title>
<link href="https://fonts.googleapis.com/css2?family=PT+Sans:ital,wght@0,400;0,700;1,700&family=PT+Sans+Narrow:wght@400;700&family=Kaushan+Script&display=swap" rel="stylesheet">
<style>
  :root {
    --navy: #1d2a6b;
    --maroon: #751a28;
    --badge: #6c1020;
    --green: #1e7a34;
    --ink: #222222;
    --frame: #3a3a3a;
    --paper: #ffffff;
  }
  * { box-sizing: border-box; margin: 0; padding: 0; }
  html, body { width: 680px; height: 1200px; overflow: hidden; background: var(--paper); }
  .banner {
    position: relative;
    width: 680px;
    height: 1200px;
    border: 2px solid var(--frame);
    background: var(--paper);
    font-family: "PT Sans", sans-serif;
    overflow: hidden;
  }
  .hero-photo {
    position: absolute;
    left: 0; top: 0;
    width: 676px; height: 396px;
    border-bottom: 2px solid var(--frame);
    background:
      radial-gradient(ellipse 60% 55% at 18% 78%, #e8cf9a 0%, rgba(232,207,154,0) 70%),
      radial-gradient(ellipse 55% 45% at 62% 38%, #f0cdb4 0%, rgba(240,205,180,0) 75%),
      linear-gradient(170deg, #f4f1ee 0%, #efd8c8 45%, #e9d0bd 70%, #ece6ef 100%);
  }
  .badge {
    position: absolute;
    left: 372px; top: 252px;
    width: 300px; height: 136px;
  }
  .badge svg { position: absolute; inset: 0; }
  .badge-text {
    position: absolute; inset: 0;
    display: flex; flex-direction: column; align-items: center; justify-content: center;
    font-family: "PT Sans Narrow", sans-serif;
    font-weight: 700;
    font-size: 36px;
    line-height: 34px;
    color: var(--paper);
    text-align: center;
    padding-left: 8px;
  }
  .stress, .relax { position: absolute; left: 17px; right: 14px; }
  .stress {
    font-family: "PT Sans Narrow", sans-serif;
    font-size: 30px;
    line-height: 38px;
    color: var(--navy);
    white-space: nowrap;
    font-weight: 700;
  }
  .stress .label { font-weight: 400; }
  .stress.tight { font-size: 28.5px; }
  .relax {
    display: grid;
    grid-template-columns: 111px 1fr;
    font-size: 29px;
    line-height: 34px;
    color: var(--ink);
  }
  .relax .label {
    font-weight: 700;
    font-style: italic;
    color: var(--maroon);
  }
  .relax .copy { text-align: justify; text-align-last: left; }
  .brand-trademark {
    font-family: "Kaushan Script", cursive;
    color: var(--green);
    font-size: 27px;
  }
  .cta {
    position: absolute;
    left: 0; right: 0; top: 1023px;
    text-align: center;
    font-family: "PT Sans Narrow", sans-serif;
    font-weight: 700;
    font-style: italic;
    font-size: 31px;
    line-height: 38px;
    color: var(--maroon);
  }
  .company {
    position: absolute;
    left: 0; right: 0; top: 1090px;
    display: flex; align-items: center; justify-content: center; gap: 14px;
  }
  .company-mark { width: 30px; height: 30px; background: var(--maroon); }
  .company-name {
    font-family: "PT Sans", sans-serif;
    font-weight: 700;
    font-size: 38px;
    color: var(--navy);
  }
</style>
</head>
<body>
<main class="banner">
  <div class="hero-photo" role="img" aria-label="Photograph of hands massaging the shoulders of a relaxed woman lying face down on a white towel"></div>

  <div class="badge">
    <svg viewBox="0 0 300 136" width="300" height="136" aria-hidden="true">
      <polygon fill="var(--badge)" stroke="#ffffff" stroke-width="3" stroke-linejoin="miter"
        points="298,68 275.6,78.1 286.8,93.3 256.4,96.9 254.6,114.7 221.2,111.2 206.7,129 175,119 150,134 125,119 93.3,129 78.8,111.2 45.4,114.7 43.6,96.9 13.2,93.3 24.4,78.1 2,68 24.4,57.9 13.2,42.7 43.6,39.1 45.4,21.3 78.8,24.8 93.3,7 125,17 150,2 175,17 206.7,7 221.2,24.8 254.6,21.3 256.4,39.1 286.8,42.7 275.6,57.9"/>
    </svg>
    <div class="badge-text"><span>FOR BOARD</span><span>MEMBERS</span></div>
  </div>

  <p class="stress" style="top:416px"><span class="label">Stress:</span> THE BOARD HAS TOO MUCH WORK TO DO</p>
  <p class="relax" style="top:454px"><span class="label">Relax…</span><span class="copy">and let us do the work.</span></p>

  <p class="stress" style="top:497px"><span class="label">Stress:</span> YOUR COMMUNITY HAS “ISSUES.”</p>
  <p class="relax" style="top:535px"><span class="label">Relax…</span><span class="copy">and let us give you a <span class="brand-trademark">Copper Lantern</span>.</span></p>

  <p class="stress" style="top:577px"><span class="label">Stress:</span> YOUR MEMBERS CANNOT PAY ONLINE.</p>
  <p class="relax" style="top:616px"><span class="label">Relax…</span><span class="copy">we’ll give your members multiple ways to pay.</span></p>

  <p class="stress tight" style="top:692px"><span class="label">Stress:</span> COMMUNICATION IS POOR OR INCONSISTENT.</p>
  <p class="relax" style="top:730px"><span class="label">Relax…</span><span class="copy">we’ll keep you informed with a robust online portal, chock full of information.</span></p>

  <p class="stress" style="top:806px"><span class="label">Stress:</span> YOUR DELINQUENCIES ARE HIGH.</p>
  <p class="relax" style="top:845px"><span class="label">Relax…</span><span class="copy">as a licensed collection agency, we have developed an effective collections program that works in tandem with your collections attorney. Plus, we can report to the credit bureau!</span></p>

  <p class="cta">COME IN TO TALK AND START RELAXING TODAY!</p>

  <div class="company">
    <span class="company-mark" aria-hidden="true"></span>
    <span class="company-name">Brindlequay Management, Inc.</span>
  </div>
</main>
</body>
</html>
```